Project Report for American Indian and Alaska Native org (U.S.)

We need a report formatted/ design / layout.
We are a nonprofit organization that works on indigenous elder issues.
The report should reflect our logo color scheme.
Body font should be at least 11 point sans serif.
Ideally, headings and title would use fonts that are reminiscent of tribal cultures though not hard to read or whimsical/ unprofessional looking.

We have used some light script style fonts in the past -- nothing too cursive looking though.

The audience is public health professionals and tribal staff and leadership.

We want our organization's logo (QV7) and the project logo (brain health) incorporated into the title page.

We prefer the files to come back to us in an editable fashion + a pdf file.

Industry/Entity Type

tribal communities and public health officials

Font styles to use
Serif
Sans Serif

Requirements
Must have
• our logo and color scheme
Should not have
• headdress images

```html
<!DOCTYPE html>
<html lang="en">
<head>
<meta charset="utf-8">
<title>Tribal Law &amp; Policy Report Layout</title>
<link rel="stylesheet" href="https://fonts.googleapis.com/css2?family=Bebas+Neue&family=Work+Sans:wght@400;500;600&family=Arimo:wght@400;700&family=Yellowtail&display=swap">
<style>
  :root{
    --teal:#4fa6b0;
    --red:#b05a50;
    --mid:#8b7f7e;
    --ink:#222222;
    --stage:#3b3a3b;
    --paper:#ffffff;
    --placeholder:#b7b7b7;
  }
  *{box-sizing:border-box;margin:0;padding:0}
  html,body{width:960px;height:1200px;overflow:hidden;background:var(--stage)}
  body{position:relative;font-family:"Work Sans",Arial,sans-serif;color:var(--ink)}
  .page{position:absolute;width:360px;height:510px;background:var(--paper);overflow:hidden;box-shadow:0 2px 6px rgba(0,0,0,.35)}
  .page--cover{left:103px;top:79px}
  .page--contents{left:497px;top:79px}
  .page--summary{left:103px;top:612px}
  .page--back{left:497px;top:612px}
  .page svg.shape{position:absolute;left:0;top:0;width:360px;height:510px}

  /* cover */
  .cover-title{position:absolute;left:35px;top:38px;font-family:"Bebas Neue",Impact,sans-serif;font-size:34px;line-height:33px;color:var(--red);letter-spacing:.2px}
  .cover-title .lead{color:var(--teal)}
  .pill{position:absolute;left:36px;background:var(--teal);color:#fff;font-family:"Work Sans",sans-serif;font-weight:600;font-size:11px;letter-spacing:.6px;padding:1px 6px 0;border-radius:0 9px 9px 0;height:15px;line-height:15px}
  .pill--prepared{top:250px}
  .pill--for{top:309px}
  .credit{position:absolute;left:36px;top:270px;color:var(--red);font-family:"Work Sans",sans-serif;font-size:11px;line-height:15px;letter-spacing:.8px}
  .credit .date{font-weight:500;letter-spacing:.5px}
  .org-mark{position:absolute;left:42px;top:352px;font-family:"Work Sans",sans-serif;font-weight:600;color:var(--teal);font-size:12px;line-height:14px;letter-spacing:.3px}
  .org-mark .code{font-size:26px;line-height:26px;display:block}
  .center-mark{position:absolute;left:42px;top:402px;display:flex;align-items:center;gap:10px;font-family:"Work Sans",sans-serif;font-weight:600;color:var(--red);font-size:11px;line-height:13px}
  .center-mark .dot{width:52px;height:52px;border-radius:50%;background:var(--teal);flex:none}

  /* running header */
  .running-head{position:absolute;left:23px;right:21px;top:30px;height:28px;border-bottom:1.5px solid var(--red);display:flex;justify-content:space-between;align-items:flex-end;padding-bottom:3px}
  .running-head h2{font-family:"Bebas Neue",Impact,sans-serif;font-weight:400;color:var(--teal);font-size:20px;line-height:20px;letter-spacing:.3px}
  .head-mark{font-family:"Work Sans",sans-serif;font-weight:600;color:var(--red);font-size:7px;line-height:8px;text-align:right;letter-spacing:.2px}
  .head-mark .code{font-size:14px;line-height:14px;display:block}

  /* contents */
  .toc{position:absolute;left:34px;top:92px;width:293px;border-collapse:collapse;font-size:8.6px;color:#222}
  .toc td{border-bottom:1px solid var(--teal);height:18.2px;vertical-align:bottom;padding:0 0 2px}
  .toc .num{width:16px;color:var(--red);text-align:center;border-right:1px solid var(--teal)}
  .toc .item{padding-left:5px}
  .toc .pg{width:16px;color:var(--red);text-align:center;border-left:1px solid var(--teal)}
  .toc tr:last-child td{border-bottom:none}

  /* footer */
  .foot-links{position:absolute;right:62px;top:475px;text-align:right;color:#fff;font-family:Arimo,Arial,sans-serif;font-size:6.5px;line-height:8.6px}
  .foot-links b{font-weight:700}
  .folio{position:absolute;left:302px;top:473px;width:18px;height:37px;background:var(--paper);font-family:Arimo,Arial,sans-serif;font-weight:700;font-size:11px;text-align:center;padding-top:4px;color:#111}

  /* summary */
  .photo-slot{position:absolute;left:24px;top:100px;width:316px;height:200px;background:var(--placeholder)}
  .summary-text{position:absolute;left:25px;top:309px;width:315px;font-family:Arimo,Arial,sans-serif;font-size:7.6px;line-height:9.4px;text-align:justify;color:#111}
  .summary-text p{margin-bottom:9px}

  /* back */
  .back-mark{position:absolute;left:230px;top:320px;display:flex;align-items:center;gap:6px;color:#fff;font-family:"Work Sans",sans-serif;font-weight:600;font-size:24px}
  .back-mark .dot{width:30px;height:30px;border-radius:50%;border:2px solid #fff}
  .thanks{position:absolute;right:52px;top:362px;font-family:Yellowtail,cursive;color:#fff;font-size:40px;line-height:44px}
  .back-contact{position:absolute;right:60px;top:422px;text-align:right;color:#fff;font-family:Arimo,Arial,sans-serif}
  .back-contact .phone{font-size:16px;font-weight:700;letter-spacing:.5px;line-height:20px}
  .back-contact .url{font-size:10px;line-height:12.5px}
</style>
</head>
<body>

<section class="page page--cover">
  <svg class="shape" viewBox="0 0 360 510" aria-hidden="true">
    <defs>
      <linearGradient id="coverFill" x1="0" y1="0" x2="0" y2="1">
        <stop offset="0" stop-color="#4fa6b0"/><stop offset=".55" stop-color="#8b7f7e"/><stop offset="1" stop-color="#b05a50"/>
      </linearGradient>
    </defs>
    <path d="M282,0 C225,60 222,160 262,250 C302,330 352,380 327,440 C312,480 277,500 252,510 L360,510 L360,0Z" fill="#b05a50"/>
    <path d="M289,0 C233,60 228,160 268,250 C308,330 358,380 333,440 C318,480 283,500 258,510 L360,510 L360,0Z" fill="#4fa6b0"/>
    <path d="M296,0 C242,60 236,160 276,250 C316,330 366,380 341,440 C326,480 291,500 266,510 L360,510 L360,0Z" fill="url(#coverFill)"/>
  </svg>
  <h1 class="cover-title"><span class="lead">Tribal Law<br>&amp; Policy:</span><br>Alzheimer’s<br>Disease and<br>Related Dementia<br>Issues</h1>
  <div class="pill pill--prepared">PREPARED BY</div>
  <p class="credit">HARLOW CONSULTING<br><span class="date">OCTOBER 27, 2021</span></p>
  <div class="pill pill--for">FOR</div>
  <div class="org-mark"><span class="code">QV7</span>COUNCIL FOR NATIVE<br>ELDER VITALITY</div>
  <div class="center-mark"><span class="dot"></span><span>NATIVE ELDERS<br>BRAIN WELLNESS<br>RESOURCE CENTER</span></div>
</section>

<section class="page page--contents">
  <header class="running-head">
    <h2>Contents</h2>
    <div class="head-mark"><span class="code">QV7</span>NATIVE ELDER VITALITY</div>
  </header>
  <table class="toc">
    <tr><td class="num">1</td><td class="item">Executive Summary</td><td class="pg">3</td></tr>
    <tr><td class="num">2</td><td class="item">Background</td><td class="pg">4</td></tr>
    <tr><td class="num">3</td><td class="item">Road Map for Indian Country</td><td class="pg">5</td></tr>
    <tr><td class="num">4</td><td class="item">Tribal Sovereignty</td><td class="pg">5</td></tr>
    <tr><td class="num">5</td><td class="item">Process</td><td class="pg">6</td></tr>
    <tr><td class="num">6</td><td class="item">Primary Sources</td><td class="pg">6</td></tr>
    <tr><td class="num">7</td><td class="item">Secondary Sources</td><td class="pg">7</td></tr>
    <tr><td class="num">8</td><td class="item">Road Map Development and Subsequent Activities</td><td class="pg">7</td></tr>
    <tr><td class="num">9</td><td class="item">Model Law Commission</td><td class="pg">7</td></tr>
    <tr><td class="num" style="height:29px">10</td><td class="item">Council of State Lawmakers<br>(Native Caucus of State Lawmakers)</td><td class="pg">7</td></tr>
    <tr><td class="num">11</td><td class="item">Results</td><td class="pg">8</td></tr>
    <tr><td class="num">12</td><td class="item">Related Policy Issues Collections</td><td class="pg">8</td></tr>
    <tr><td class="num">13</td><td class="item">State Alzheimer Plans</td><td class="pg">9</td></tr>
    <tr><td class="num">14</td><td class="item">National Plan to Address Alzheimer's Disease</td><td class="pg">11</td></tr>
    <tr><td class="num">15</td><td class="item">Other National Plans</td><td class="pg">11</td></tr>
    <tr><td class="num">16</td><td class="item">Conclusion</td><td class="pg">11</td></tr>
    <tr><td class="num">17</td><td class="item">Citations 1</td><td class="pg">12</td></tr>
  </table>
  <svg class="shape" viewBox="0 0 360 510" aria-hidden="true">
    <defs>
      <linearGradient id="footFillA" x1="0" y1="0" x2="1" y2="0">
        <stop offset="0" stop-color="#b05a50"/><stop offset=".5" stop-color="#8b7f7e"/><stop offset="1" stop-color="#4fa6b0"/>
      </linearGradient>
    </defs>
    <path d="M0,436 C40,480 80,492 120,484 C190,468 230,424 290,430 C320,434 345,448 360,458 L360,510 L0,510Z" fill="#b05a50"/>
    <path d="M0,442 C40,486 80,498 120,490 C190,474 230,430 290,436 C320,440 345,454 360,464 L360,510 L0,510Z" fill="#4fa6b0"/>
    <path d="M0,448 C40,492 80,503 120,495 C190,479 230,437 290,442 C320,446 345,460 360,470 L360,510 L0,510Z" fill="url(#footFillA)"/>
  </svg>
  <p class="foot-links"><b>www.NativeBrainWellness</b>.org<br>www.<b>nphagency</b>.org/aging</p>
  <div class="folio">2</div>
</section>

<section class="page page--summary">
  <header class="running-head">
    <h2>Executive Summary</h2>
    <div class="head-mark"><span class="code">QV7</span>NATIVE ELDER VITALITY</div>
  </header>
  <div class="photo-slot" role="img" aria-label="Photograph placeholder for the executive summary"></div>
  <div class="summary-text">
    <p>From the beginning of persons organizing action on dementia and caregiving issues in the early 1980s, working in and through government as one means of dealing with the myriad problems related to the societal burden and trajectory has been a means to an end of better lives for persons living with Alzheimer's disease and related dementias (ADRD). This brief examines how federal and tribal law and state policy actions currently address these issues.</p>
    <p>As sovereign nations, tribes are uniquely situated to use law as a public health tool to promote the health and well-being of their communities. Additionally, federal law creates a framework that governs the relationships among tribes, states, and the federal government that can affect tribal public health.</p>
    <p>National Public Health Agency (2017)</p>
  </div>
  <svg class="shape" viewBox="0 0 360 510" aria-hidden="true">
    <defs>
      <linearGradient id="footFillB" x1="0" y1="0" x2="1" y2="0">
        <stop offset="0" stop-color="#b05a50"/><stop offset=".5" stop-color="#8b7f7e"/><stop offset="1" stop-color="#4fa6b0"/>
      </linearGradient>
    </defs>
    <path d="M0,436 C40,480 80,492 120,484 C190,468 230,424 290,430 C320,434 345,448 360,458 L360,510 L0,510Z" fill="#b05a50"/>
    <path d="M0,442 C40,486 80,498 120,490 C190,474 230,430 290,436 C320,440 345,454 360,464 L360,510 L0,510Z" fill="#4fa6b0"/>
    <path d="M0,448 C40,492 80,503 120,495 C190,479 230,437 290,442 C320,446 345,460 360,470 L360,510 L0,510Z" fill="url(#footFillB)"/>
  </svg>
  <p class="foot-links"><b>www.NativeBrainWellness</b>.org<br>www.<b>nphagency</b>.org/aging</p>
  <div class="folio">3</div>
</section>

<section class="page page--back">
  <svg class="shape" viewBox="0 0 360 510" aria-hidden="true">
    <defs>
      <linearGradient id="backFill" x1="0" y1="0" x2="0" y2="1">
        <stop offset="0" stop-color="#4fa6b0"/><stop offset=".5" stop-color="#8b7f7e"/><stop offset="1" stop-color="#b05a50"/>
      </linearGradient>
    </defs>
    <path d="M66,0 C110,30 118,70 108,120 C92,190 30,250 24,330 C18,400 60,470 98,510 L360,510 L360,0Z" fill="#4fa6b0"/>
    <path d="M72,0 C116,30 124,70 114,120 C98,190 37,250 31,330 C25,400 66,470 104,510 L360,510 L360,0Z" fill="#b05a50"/>
    <path d="M79,0 C122,30 130,70 120,120 C104,190 44,250 38,330 C32,400 73,470 112,510 L360,510 L360,0Z" fill="url(#backFill)"/>
  </svg>
  <div class="back-mark">QV7<span class="dot"></span></div>
  <p class="thanks">Thank You</p>
  <div class="back-contact">
    <p class="phone">123.456.7890</p>
    <p class="url">www.<b>NativeBrainWellness</b>.org</p>
    <p class="url">www.<b>nphagency</b>.org/aging</p>
  </div>
</section>

</body>
</html>
```